New logo and wordpress design for Brightmoor-hub.org

We run a website that collates profiles/interviews of individuals who have completed a PhD and moved away from a traditional academix career path into something related. This is often related to the field they studied in, such as publishing, government policy, consulting, teaching and many other things. The website https://brightmoor-hub.org aims to give students and researchers ideas about what paths they can take their career on.

We would like to refresh our brand with a new website and logo. Our website is run through wordpress and hence we would need appropriate files and designs to accomodate this.
Our new logo should represent the idea of navigating a career path and exploring the unknown. Up until now it has been a compass in tones of purple and blue. We are happy to keep this motif but would need an updated, more representative logo. We are also happy to get some new ideas if the designer has something they think would fit.
The website itself should have fresh and clean look. We would like a banner at the top with clear links to the various parts of the site. The banner should stay consistent throughout the site.
We would like the main page to have a clean and simple look which places the focus on the profiles and their associated photos.
We would like pictographs to represent the different fields which our profiles fit into and would like to discuss with the winning designer what these would look like exactly. As a starting point we would like pictographs representing STEM (Science, Technology, Engineering, Mathematics) and SHAPE (Social Sciences, Humanities and Arts for People and the Economy).

We are really looking for something that is clean and professional but embodies our mission to represent all of the major industries which doctoral graduates can go on to work in. Those being, academia (universities), government, industry (private enterprise and companies), and third sector (Charities and think tanks etc.). Any design should cover all of these and not focus just on a big business or similar. It should also represent that we are not purely science focused, but all disciplines and are a broad church in that sense. We are open to various colour schemes and ideas but would like something that gives a professional but approachable feel, it should have elements of Oxford, but not suggest that we are only open to Calderwick University students or graduates.
Some sites that may be useful are:
https://kestrelguild.org/news-resources/projects/research-culture/ - talks about the different areas of employment we are trying to represent
https://www.famden-lv.ac.uk/ an oxford internal website that we like the presentation of.

Target Market(s)

Academic researchers with a PhD

Industry/Entity Type

Academic Careers

Colors
0054AA
0677BA
7BADD7
CADEEF
E8F1F8
00AB8E
00BBA5
67D7C9
C6EFE9
E9F9F6
FFF300
FFF600
FEFA6F
FFFEC7
FFFEE8
6B429C
8869AF
B7A5CE
E3DAEB
F3F0F8

Requirements
Must have
• A new logo
Should not have
• The existing logo

```html
<!DOCTYPE html>
<html lang="en">
<head>
<meta charset="UTF-8">
<title>Brightmoor Hub – Explore Your Options Beyond Academia</title>
<link rel="stylesheet" href="https://fonts.googleapis.com/css2?family=Poppins:wght@300;400;500;600&display=swap">
<style>
:root{
  --teal:#15a98c;
  --teal-dark:#0f8f80;
  --teal-soft:#6fcdb8;
  --green-accent:#2fd08f;
  --ink:#1b1b1b;
  --text:#555b60;
  --muted:#8a9096;
  --line:#c9ccd0;
  --panel:#ffffff;
  --light-bg:#f6f7f7;
  --footer:#1a1a1b;
  --footer-text:#b9bcbf;
  --label-blue:#4f5fa6;
}
*{box-sizing:border-box;margin:0;padding:0}
html,body{width:1200px;height:3203px;overflow:hidden}
body{font-family:'Poppins',sans-serif;background:#fff;color:var(--ink);position:relative}
.abs{position:absolute}
.btn{position:absolute;display:flex;align-items:center;justify-content:center;background:var(--teal);color:#fff;border-radius:30px;font-weight:500;text-transform:uppercase;letter-spacing:.2px}

/* hero */
.hero-bg{left:0;top:0;width:1200px;height:693px;background:linear-gradient(135deg,#2cb3a5 0%,#1c9f95 45%,#15938b 100%)}
.hero-photo{left:560px;top:0;width:640px;height:605px;clip-path:polygon(90px 0,640px 0,640px 605px,0 605px);background:linear-gradient(160deg,#e6e9ea 0%,#c8ccd0 40%,#474c55 70%,#f0a534 100%)}
.header{left:82px;top:4px;width:955px;height:85px;background:#fff;display:flex;align-items:center}
.logo-name{font-weight:600;font-size:27px;color:var(--teal);display:flex;align-items:center;gap:8px;white-space:nowrap}
.logo-dot{width:10px;height:10px;border-radius:50%;background:var(--teal)}
.header .logo-name{position:absolute;left:26px;top:24px}
.nav{position:absolute;left:324px;top:34px;font-size:13.5px;font-weight:500;color:#222}
.nav span{position:absolute;white-space:nowrap}
.search-box{left:1037px;top:4px;width:77px;height:85px;background:var(--teal);display:flex;align-items:center;justify-content:center}
.hero-title{left:87px;top:218px;font-size:49px;font-weight:600;color:#fff;line-height:55px;white-space:nowrap}
.hero-title .accent{color:var(--green-accent)}
.hero-sub{left:94px;top:334px;width:480px;font-size:19.5px;line-height:26px;color:#fff;font-weight:400}
.hero-btn{left:94px;top:414px;width:188px;height:41px;font-size:16px}

/* feature cards */
.features{left:86px;top:605px;width:1032px;height:180px;background:var(--panel);box-shadow:0 10px 30px rgba(0,0,0,.08)}
.feature{position:absolute;top:0;height:180px}
.feature-img{position:absolute;top:37px;width:112px;height:112px;border-radius:50%}
.feature h3{position:absolute;font-size:17px;font-weight:500;white-space:nowrap}
.feature p{position:absolute;font-size:11px;line-height:15px;color:var(--muted);width:185px}
.feature .mini-btn{position:absolute;height:24px;width:111px;background:var(--teal);border-radius:14px;color:#fff;font-size:9px;font-weight:600;display:flex;align-items:center;justify-content:center}

/* intro */
.intro-img{left:43px;top:883px;width:494px;height:374px;clip-path:polygon(0 0,494px 0,451px 374px,0 374px);background:linear-gradient(180deg,#8d969c 0%,#c9d0d2 40%,#57b9d4 70%,#9bb088 100%)}
.intro-title{left:604px;top:942px;width:570px;font-size:24px;line-height:28px;font-weight:400;color:#111}
.intro-text{left:606px;top:1016px;width:545px;font-size:15.5px;line-height:28.5px;color:var(--text);font-weight:300}
.intro-btn{left:604px;top:1189px;width:186px;height:41px;font-size:16px}

/* profiles */
.profiles-band{left:4px;top:1364px;width:1188px;height:543px;background:linear-gradient(180deg,#6dcbb5 0%,#5fc5b3 50%,#55c4b7 100%)}
.profiles-title{left:0;top:1462px;width:1258px;text-align:center;font-size:28px;font-weight:600;color:#fff}
.profile-card{position:absolute;top:1571px;width:217px;height:432px;background:#fff;border:1px solid #d7dcdc;border-radius:108px}
.profile-photo{position:absolute;left:17px;top:18px;width:182px;height:182px;border-radius:50%;border:6px solid var(--teal-soft);background:linear-gradient(180deg,#8b7e78,#4f4a4a)}
.profile-name{position:absolute;left:16px;top:236px;font-size:15.5px;font-weight:500;white-space:nowrap;color:#111}
.profile-role{position:absolute;left:17px;top:259px;font-size:8px;color:var(--label-blue);white-space:nowrap}
.profile-bio{position:absolute;left:17px;top:273px;width:190px;font-size:8px;line-height:10px;color:var(--muted)}
.profile-meta{position:absolute;left:19px;font-size:8.5px;color:var(--muted);white-space:nowrap}
.profile-meta b{font-weight:500;color:#222}
.profile-arrow{position:absolute;left:82px;top:406px;width:52px;height:52px;border-radius:50%;background:var(--teal);display:flex;align-items:center;justify-content:center}

/* contact */
.contact-bg{left:4px;top:2171px;width:1196px;height:491px;background:var(--light-bg)}
.contact-photo{left:627px;top:2171px;width:573px;height:491px;clip-path:polygon(106px 0,573px 0,573px 491px,0 491px);background:linear-gradient(150deg,#eef1ee 0%,#cfd5d6 40%,#3a4250 80%,#2a303a 100%)}
.contact-title{left:86px;top:2252px;font-size:27px;font-weight:500;color:#111}
.field{position:absolute;border:1.5px solid var(--line);background:#fff;font-size:9.5px;color:#9a9ea2;padding:8px 16px}
.send-btn{left:87px;top:2549px;width:186px;height:41px;font-size:16px}

/* footer */
.footer{left:4px;top:2668px;width:1196px;height:535px;background:var(--footer)}
.footer .logo-name{position:absolute;left:46px;top:136px;font-size:34px;color:var(--teal)}
.footer-tag{left:55px;top:2860px;width:330px;font-size:15.5px;line-height:28px;color:var(--footer-text);font-weight:300}
.social{left:62px;top:2932px;width:37px;height:37px;border-radius:50%;background:#1da1f2}
.col-head{position:absolute;font-size:23px;font-weight:500;color:var(--teal);white-space:nowrap}
.link{position:absolute;font-size:14.5px;color:#e2e4e6;white-space:nowrap;display:flex;align-items:center;gap:16px}
.link::before{content:"→";color:var(--teal);font-size:14px}
.sub-input{left:881px;top:2873px;width:233px;height:52px;border-radius:30px;background:#fff;font-size:15.5px;color:#666;display:flex;align-items:center;padding-left:25px}
.sub-btn{left:881px;top:2945px;width:233px;height:50px;font-size:17px;font-weight:600}
.copyright{left:82px;top:3157px;font-size:13.5px;color:#6e7276;font-weight:300}
.legal{left:900px;top:3157px;font-size:13.5px;color:#6e7276;font-weight:300}
</style>
</head>
<body>

<!-- hero -->
<div class="abs hero-bg" role="img" aria-label="Teal faceted background"></div>
<div class="abs hero-photo" role="img" aria-label="Photo of two professionals reviewing an orange folder"></div>

<header class="abs header">
  <div class="logo-name"><span class="logo-dot"></span>Brightmoor Hub</div>
  <nav class="nav">
    <span style="left:0">HOME</span>
    <span style="left:78px">PROFILES</span>
    <span style="left:180px">GET INVOLVED</span>
    <span style="left:326px">EVENTS</span>
    <span style="left:416px">RESOURCES</span>
    <span style="left:534px">ABOUT US</span>
  </nav>
</header>
<div class="abs search-box">
  <svg width="28" height="28" viewBox="0 0 28 28" fill="none" stroke="#fff" stroke-width="2.5"><circle cx="11.5" cy="11.5" r="8.5"/><line x1="18" y1="18" x2="26" y2="26" stroke-linecap="round"/></svg>
</div>

<h1 class="abs hero-title">Explore Your Options<br><span class="accent">Beyond</span> Academia</h1>
<p class="abs hero-sub">A collection of profiles of people who have made the transition from academia to industry.</p>
<a class="btn hero-btn">Get Involved</a>

<section class="abs features">
  <div class="feature" style="left:0;width:340px">
    <div class="feature-img" role="img" aria-label="Photo of a handshake" style="left:33px;background:linear-gradient(135deg,#c58b6a,#2c6fa3)"></div>
    <h3 style="left:170px;top:52px">Career profiles</h3>
    <p style="left:171px;top:78px">Explore a collection of profiles from researchers pursuing careers beyond academia.</p>
    <div class="mini-btn" style="left:174px;top:136px">EXPLORE PROFILES</div>
  </div>
  <div class="feature" style="left:340px;width:340px">
    <div class="feature-img" role="img" aria-label="Photo of a domed university building" style="left:47px;background:linear-gradient(180deg,#8fb7d8,#a89072 60%,#5c6e4c)"></div>
    <h3 style="left:176px;top:56px">About Us</h3>
    <p style="left:176px;top:81px">EThis website is edited by a group of DPhil students and researchers connected to Calderwick University.</p>
    <div class="mini-btn" style="left:178px;top:139px">WHO WE ARE</div>
  </div>
  <div class="feature" style="left:680px;width:352px">
    <div class="feature-img" role="img" aria-label="Photo of hands typing on a laptop" style="left:38px;top:34px;background:linear-gradient(135deg,#d7dadc,#5a5f66)"></div>
    <h3 style="left:168px;top:55px">Get Involved</h3>
    <p style="left:169px;top:80px;width:170px">See how you can contribute to the Brightmoor Hub: Options Beyond Academia project.</p>
    <div class="mini-btn" style="left:173px;top:139px">FIND OUT HOW</div>
  </div>
</section>

<!-- intro -->
<div class="abs intro-img" role="img" aria-label="Photo of medical professionals walking together"></div>
<h2 class="abs intro-title">Researchers find all sorts of rewarding careers – smart people work everywhere!</h2>
<p class="abs intro-text">Such diversity in potential roles can prove challenging when exploring your options. This collection of career profiles enables you to see what others in your position chose to do, why and how they made the move, and what they most enjoy about their job. You will get a feel for their daily activities, workplace culture and work-life balance.</p>
<a class="btn intro-btn">Read More</a>

<!-- recent profiles -->
<div class="abs profiles-band" role="img" aria-label="Faded teal-tinted office photo"></div>
<h2 class="abs profiles-title">RECENT PROFILES</h2>

<article class="profile-card" style="left:102px">
  <div class="profile-photo" role="img" aria-label="Profile portrait"></div>
  <div class="profile-name">Marisol Ortega-Vane</div>
  <div class="profile-role">Behavioural Scientist at Fenwick Lab</div>
  <div class="profile-bio">My favorite parts of my job include developing behavioral solutions and running trials</div>
  <div class="profile-meta" style="top:308px"><b>Career Profiles:</b>&nbsp; PHD &nbsp; <b>Degree:</b> Psychology</div>
  <div class="profile-meta" style="top:326px"><b>Left academia after:</b> 6+ years postdoc</div>
  <div class="profile-meta" style="top:345px"><b>Sector:</b>&nbsp; Charities</div>
  <div class="profile-arrow"><svg width="24" height="24" viewBox="0 0 24 24"><path d="M3 9h9V3l10 9-10 9v-6H3z" fill="#fff"/></svg></div>
</article>
<article class="profile-card" style="left:367px">
  <div class="profile-photo" role="img" aria-label="Profile portrait" style="background:linear-gradient(180deg,#6b8fa0,#2b3350)"></div>
  <div class="profile-name">Marisol Ortega-Vane</div>
  <div class="profile-role">Behavioural Scientist at Fenwick Lab</div>
  <div class="profile-bio">My favorite parts of my job include developing behavioral solutions and running trials</div>
  <div class="profile-meta" style="top:308px"><b>Career Profiles:</b>&nbsp; PHD &nbsp; <b>Degree:</b> Psychology</div>
  <div class="profile-meta" style="top:326px"><b>Left academia after:</b> 6+ years postdoc</div>
  <div class="profile-meta" style="top:345px"><b>Sector:</b>&nbsp; Charities</div>
  <div class="profile-arrow"><svg width="24" height="24" viewBox="0 0 24 24"><path d="M3 9h9V3l10 9-10 9v-6H3z" fill="#fff"/></svg></div>
</article>
<article class="profile-card" style="left:632px">
  <div class="profile-photo" role="img" aria-label="Profile portrait" style="background:linear-gradient(180deg,#9aa3a8,#2a3346)"></div>
  <div class="profile-name">Marisol Ortega-Vane</div>
  <div class="profile-role">Behavioural Scientist at Fenwick Lab</div>
  <div class="profile-bio">My favorite parts of my job include developing behavioral solutions and running trials</div>
  <div class="profile-meta" style="top:308px"><b>Career Profiles:</b>&nbsp; PHD &nbsp; <b>Degree:</b> Psychology</div>
  <div class="profile-meta" style="top:326px"><b>Left academia after:</b> 6+ years postdoc</div>
  <div class="profile-meta" style="top:345px"><b>Sector:</b>&nbsp; Charities</div>
  <div class="profile-arrow"><svg width="24" height="24" viewBox="0 0 24 24"><path d="M3 9h9V3l10 9-10 9v-6H3z" fill="#fff"/></svg></div>
</article>
<article class="profile-card" style="left:897px">
  <div class="profile-photo" role="img" aria-label="Profile portrait" style="background:linear-gradient(180deg,#e6e4e0,#c98f8a)"></div>
  <div class="profile-name">Marisol Ortega-Vane</div>
  <div class="profile-role">Behavioural Scientist at Fenwick Lab</div>
  <div class="profile-bio">My favorite parts of my job include developing behavioral solutions and running trials</div>
  <div class="profile-meta" style="top:308px"><b>Career Profiles:</b>&nbsp; PHD &nbsp; <b>Degree:</b> Psychology</div>
  <div class="profile-meta" style="top:326px"><b>Left academia after:</b> 6+ years postdoc</div>
  <div class="profile-meta" style="top:345px"><b>Sector:</b>&nbsp; Charities</div>
  <div class="profile-arrow"><svg width="24" height="24" viewBox="0 0 24 24"><path d="M3 9h9V3l10 9-10 9v-6H3z" fill="#fff"/></svg></div>
</article>

<!-- contact -->
<div class="abs contact-bg"></div>
<div class="abs contact-photo" role="img" aria-label="Photo of three business people in a meeting"></div>
<h2 class="abs contact-title">CONTACT US</h2>
<div class="field" style="left:87px;top:2315px;width:242px;height:30px">Name</div>
<div class="field" style="left:347px;top:2315px;width:242px;height:30px">Phone</div>
<div class="field" style="left:87px;top:2359px;width:242px;height:29px">Email</div>
<div class="field" style="left:347px;top:2359px;width:242px;height:29px">Subject</div>
<div class="field" style="left:87px;top:2410px;width:502px;height:105px;padding:16px 26px">Message</div>
<a class="btn send-btn">Send Now</a>

<!-- footer -->
<footer class="abs footer">
  <div class="logo-name"><span class="logo-dot"></span>Brightmoor Hub</div>
</footer>
<p class="abs footer-tag">Such diversity in potential roles can prove challenging when exploring your options.</p>
<div class="abs social" role="img" aria-label="Social link"></div>

<div class="col-head" style="left:422px;top:2802px">Company</div>
<div class="link" style="left:428px;top:2862px">HOME</div>
<div class="link" style="left:428px;top:2913px">ABOUT</div>
<div class="link" style="left:428px;top:2957px">PROFILES</div>
<div class="link" style="left:428px;top:3005px">BLOG</div>
<div class="link" style="left:428px;top:3053px">CONTACT</div>

<div class="col-head" style="left:643px;top:2802px">Quick Links</div>
<div class="link" style="left:651px;top:2862px">FAQS</div>
<div class="link" style="left:651px;top:2909px">Privacy Policy</div>
<div class="link" style="left:651px;top:2957px">Cookies Policy</div>
<div class="link" style="left:651px;top:3005px">Term &amp; Conditions</div>

<div class="col-head" style="left:871px;top:2802px">Get Latest Updates</div>
<div class="abs sub-input">Email Address</div>
<a class="btn sub-btn">Subscribe Now</a>

<div class="abs copyright">© Copyright 2024, All Rights Reserved.</div>
<div class="abs legal">Privacy Policy | Term &amp; Conditions</div>

</body>
</html>
```